Label design for olive oil and other oils

We are a company located in Melbourne, doing the international trade, now we are starting a olive oil project and need a label for our product. Our olive oil named "Blue Heron", our products is produce in Australia and will export oversea, The label should be brief and clear. We offer the natural and premium products to our customers. The bottles of the oil will be 500ml, 750ml and 1L. Our label will use for other kinds of oil in the future, such as the nut oil, almond oil and macadamia oil, so we would like the design can be expand to other oil as well, so a series of oil label will be welcomed.

Target Market(s)

Australia local market and oversea.

Industry/Entity Type

Food Store

Requirements
Must have
• none
Nice to have
• The blue heron bird
Should not have
• none

```html
<!DOCTYPE html>
<html lang="en">
<head>
<meta charset="utf-8">
<title>Blue Heron Oils – Label Series</title>
<link href="https://fonts.googleapis.com/css2?family=Ubuntu:ital,wght@0,300;0,400;1,300&display=swap" rel="stylesheet">
<style>
  :root {
    --page: #ffffff;
    --glass-dark: #2b280b;
    --glass-mid: #4d4816;
    --glass-light: #6d6621;
    --cap-dark: #1d1b0f;
    --cap-light: #3a3722;
    --brand-red: #e0231c;
    --label-white: #f4f1e4;
    --olive-green: #8a9a1e;
    --swirl-olive: #8d8a3a;
    --swirl-copper: #a9794a;
  }
  * { margin: 0; padding: 0; box-sizing: border-box; }
  html, body {
    width: 778px;
    height: 1200px;
    overflow: hidden;
    background: var(--page);
  }
  .canvas {
    position: relative;
    width: 778px;
    height: 1200px;
    background: var(--page);
    font-family: "Ubuntu", sans-serif;
  }
  .bottles {
    position: absolute;
    left: 0; top: 0;
  }
  .bottle-label {
    position: absolute;
    top: 0;
  }
  .bottle-label--large { left: 65px; width: 312px; }
  .bottle-label--small { left: 475px; width: 215px; }

  .origin-mark {
    position: absolute;
    left: 50%;
    transform: translateX(-50%);
    border-radius: 4px;
    background: radial-gradient(ellipse, rgba(255,255,255,0.7), rgba(255,255,255,0.2));
  }
  .bottle-label--large .origin-mark { top: 150px; width: 38px; height: 28px; }
  .bottle-label--small .origin-mark { top: 282px; width: 26px; height: 20px; }

  .emblem {
    position: absolute;
    left: 50%;
    transform: translateX(-50%);
    border-radius: 40% 40% 50% 50%;
  }
  .bottle-label--large .emblem {
    top: 385px; width: 160px; height: 485px;
    background: linear-gradient(180deg, var(--swirl-olive) 0%, rgba(141,138,58,0.45) 50%, rgba(224,35,28,0.7) 72%, rgba(224,35,28,0.3) 100%);
  }
  .bottle-label--small .emblem {
    top: 395px; width: 100px; height: 380px;
    background: linear-gradient(180deg, var(--swirl-copper) 0%, rgba(169,121,74,0.45) 50%, rgba(224,35,28,0.7) 72%, rgba(224,35,28,0.3) 100%);
  }

  .brand-name, .oil-type {
    position: absolute;
    left: 0; right: 0;
    text-align: center;
    white-space: nowrap;
    line-height: 1;
  }
  .brand-name { color: var(--brand-red); font-weight: 400; }
  .oil-type { color: var(--label-white); font-weight: 300; font-style: italic; }

  .bottle-label--large .brand-name { top: 898px; font-size: 28px; }
  .bottle-label--large .oil-type { top: 938px; font-size: 30px; }
  .bottle-label--small .brand-name { top: 852px; font-size: 19px; }
  .bottle-label--small .oil-type { top: 880px; font-size: 20px; }

  .olive-icon { position: absolute; left: 50%; top: 1020px; transform: translateX(-50%); }
  .nut-icon { position: absolute; left: 50%; top: 935px; transform: translateX(-50%); }
</style>
</head>
<body>
  <main class="canvas">
    <svg class="bottles" width="778" height="1200" viewBox="0 0 778 1200" aria-hidden="true">
      <defs>
        <linearGradient id="glass-large" x1="65" y1="0" x2="377" y2="0" gradientUnits="userSpaceOnUse">
          <stop offset="0" stop-color="var(--glass-dark)"/>
          <stop offset="0.3" stop-color="var(--glass-mid)"/>
          <stop offset="0.55" stop-color="var(--glass-light)"/>
          <stop offset="0.8" stop-color="var(--glass-mid)"/>
          <stop offset="1" stop-color="var(--glass-dark)"/>
        </linearGradient>
        <linearGradient id="glass-small" x1="475" y1="0" x2="690" y2="0" gradientUnits="userSpaceOnUse">
          <stop offset="0" stop-color="var(--glass-dark)"/>
          <stop offset="0.3" stop-color="var(--glass-mid)"/>
          <stop offset="0.55" stop-color="var(--glass-light)"/>
          <stop offset="0.8" stop-color="var(--glass-mid)"/>
          <stop offset="1" stop-color="var(--glass-dark)"/>
        </linearGradient>
        <linearGradient id="cap" x1="0" y1="0" x2="1" y2="0">
          <stop offset="0" stop-color="var(--cap-dark)"/>
          <stop offset="0.5" stop-color="var(--cap-light)"/>
          <stop offset="1" stop-color="var(--cap-dark)"/>
        </linearGradient>
      </defs>

      <g class="bottle bottle--large">
        <path class="bottle-glass" fill="url(#glass-large)"
          d="M176 130 L266 130 L268 182 C270 235 377 238 377 300 L377 1148 Q377 1168 357 1168 L85 1168 Q65 1168 65 1148 L65 300 C65 238 172 235 174 182 Z"/>
        <rect class="bottle-cap" x="168" y="48" width="106" height="94" rx="9" fill="url(#cap)"/>
        <rect class="bottle-cap-rim" x="168" y="128" width="106" height="6" fill="#14130a"/>
      </g>

      <g class="bottle bottle--small">
        <path class="bottle-glass" fill="url(#glass-small)"
          d="M553 262 L611 262 L613 302 C615 345 690 350 690 400 L690 1138 Q690 1155 673 1155 L492 1155 Q475 1155 475 1138 L475 400 C475 350 550 345 552 302 Z"/>
        <rect class="bottle-cap" x="547" y="208" width="70" height="62" rx="7" fill="url(#cap)"/>
        <rect class="bottle-cap-rim" x="547" y="260" width="70" height="4" fill="#14130a"/>
      </g>
    </svg>

    <section class="bottle-label bottle-label--large">
      <div class="origin-mark" role="img" aria-label="Small map of Australia origin mark"></div>
      <div class="emblem" role="img" aria-label="Heron emblem in red line work beneath rising olive-toned swirls"></div>
      <p class="brand-name">Blue Heron</p>
      <p class="oil-type">olive oil</p>
      <svg class="olive-icon" width="34" height="40" viewBox="0 0 34 40" aria-hidden="true">
        <ellipse cx="17" cy="20" rx="13" ry="16" fill="none" stroke="var(--olive-green)" stroke-width="3"/>
      </svg>
    </section>

    <section class="bottle-label bottle-label--small">
      <div class="origin-mark" role="img" aria-label="Small map of Australia origin mark"></div>
      <div class="emblem" role="img" aria-label="Heron emblem in red line work beneath rising copper-toned swirls"></div>
      <p class="brand-name">Blue Heron</p>
      <p class="oil-type">almond oil</p>
      <svg class="nut-icon" width="24" height="28" viewBox="0 0 24 28" aria-hidden="true">
        <path d="M3 10 Q12 3 21 10" fill="none" stroke="var(--swirl-copper)" stroke-width="2.5"/>
        <path d="M5 11 L19 11 Q19 22 12 26 Q5 22 5 11 Z" fill="none" stroke="var(--swirl-copper)" stroke-width="2.5"/>
      </svg>
    </section>
  </main>
</body>
</html>
```